Original business card of a small accounting firm

My firm specializes in accounting and taxes for small businesses. I'm looking for an original and creative business card as a marketing tool to give to prospective clients; however since we are a professional firm the card must also appear professional. I'm uploading a few examples of what I believe may fit my needs. Please feel free to use them as a jumping off point. Lastly, I'm uploading the company logo which I'd like to be the focal point on the back of the card and somewhat incorporated on the front on a smaller scale. I hope my description was helpful.
Target Market(s)
Tax clients and small businesses
Industry/Entity Type
Accounting
Contact Information for Business Card
Leonard Whitcombe
Certified Public Accountant │President
Kestrel Advisors
T│ (555) 418-2763
Email│LWhitcombe@KestrelAdvisors.example

```html
<!DOCTYPE html>
<html lang="en">
<head>
<meta charset="utf-8">
<title>Kestrel Advisors — Business Card</title>
<link href="https://fonts.googleapis.com/css2?family=Open+Sans:wght@400;600;700&display=swap" rel="stylesheet">
<style>
  :root {
    --page-bg: #e9eaec;
    --card-white: #ffffff;
    --card-shadow: rgba(30, 35, 45, 0.22);
    --brand-blue: #2f78cf;
    --brand-blue-light: #3ea4e6;
    --brand-blue-deep: #1f5fb8;
    --band-grey: #6e7073;
    --ink-dark: #4a4b4d;
    --ink-light: #ffffff;
  }
  * { margin: 0; padding: 0; box-sizing: border-box; }
  html, body {
    width: 1200px; height: 901px; overflow: hidden;
    background: var(--page-bg);
    font-family: "Open Sans", Arial, sans-serif;
  }
  .stage { position: relative; width: 1200px; height: 901px; }
  .card {
    position: absolute; top: 153px;
    width: 340px; height: 595px;
    border-radius: 26px; overflow: hidden;
    background: var(--card-white);
    box-shadow: 0 10px 30px var(--card-shadow);
  }
  .card--front { left: 190px; }
  .card--back { left: 670px; }

  .card-art { position: absolute; inset: 0; width: 100%; height: 100%; }

  .brand {
    position: absolute; left: 0; right: 0; top: 58px;
    text-align: center;
  }
  .brand-line {
    display: inline-flex; align-items: center; gap: 10px;
    color: var(--ink-dark); font-weight: 700; font-size: 25px; letter-spacing: -0.2px;
  }
  .brand-mark {
    width: 20px; height: 20px; background: var(--brand-blue);
  }
  .brand-tagline {
    margin-top: 6px;
    font-size: 8.5px; letter-spacing: 2px; text-transform: uppercase;
    color: var(--ink-dark); font-weight: 400;
  }

  .contact-block {
    position: absolute; left: 34px; top: 300px; right: 20px;
    color: var(--ink-light);
  }
  .person-name {
    font-weight: 700; font-size: 19px; letter-spacing: 0.3px; text-transform: uppercase;
  }
  .person-title { font-size: 13px; margin-top: 4px; margin-left: 16px; }
  .contact-list { list-style: none; margin-top: 46px; }
  .contact-item {
    display: flex; align-items: center; gap: 8px;
    font-size: 12.5px; margin-bottom: 9px; white-space: nowrap;
  }
  .contact-icon { width: 14px; height: 14px; flex: none; }

  .back-brand {
    position: absolute; left: 0; right: 0; top: 50%;
    transform: translateY(-50%); text-align: center;
  }
  .back-brand .brand-line { font-size: 30px; gap: 12px; }
  .back-brand .brand-mark { width: 26px; height: 26px; }
</style>
</head>
<body>
<main class="stage">

  <section class="card card--front" aria-label="Front of business card">
    <svg class="card-art" viewBox="0 0 340 595" aria-hidden="true">
      <defs>
        <radialGradient id="frontBlue" cx="0.6" cy="0.25" r="0.9">
          <stop offset="0" stop-color="var(--brand-blue-light)"/>
          <stop offset="1" stop-color="var(--brand-blue-deep)"/>
        </radialGradient>
        <linearGradient id="stripeBlue" x1="0" x2="1">
          <stop offset="0" stop-color="var(--brand-blue-deep)"/>
          <stop offset="1" stop-color="var(--brand-blue-light)"/>
        </linearGradient>
      </defs>
      <path d="M0 214 Q150 160 340 168 L340 174 Q150 172 0 224 Z" fill="url(#stripeBlue)"/>
      <path d="M0 232 Q150 178 340 182 L340 196 Q160 196 0 268 Z" fill="var(--band-grey)"/>
      <path d="M0 262 Q160 192 340 194 L340 595 L0 595 Z" fill="url(#frontBlue)"/>
    </svg>

    <header class="brand">
      <div class="brand-line"><span class="brand-mark"></span>Kestrel Advisors</div>
      <p class="brand-tagline">Small business accounting and taxes</p>
    </header>

    <div class="contact-block">
      <h1 class="person-name">Leonard Whitcombe</h1>
      <p class="person-title">Managing Director</p>
      <ul class="contact-list">
        <li class="contact-item">
          <svg class="contact-icon" viewBox="0 0 16 16" aria-hidden="true"><path fill="currentColor" d="M3.6 1.5l2.2 2.6-1.3 1.7c.9 2 2.4 3.6 4.5 4.6l1.7-1.3 2.6 2.2-1.1 2.2C7.3 13.2 2.8 8.7 1.4 2.6z"/></svg>
          <span>(555) 418-2763</span>
        </li>
        <li class="contact-item">
          <svg class="contact-icon" viewBox="0 0 16 16" aria-hidden="true"><rect x="1" y="3" width="14" height="10" fill="currentColor"/><path d="M1.5 3.5L8 9l6.5-5.5" stroke="var(--brand-blue)" stroke-width="1.3" fill="none"/></svg>
          <span>LWhitcombe@KestrelAdvisors.example</span>
        </li>
        <li class="contact-item">
          <svg class="contact-icon" viewBox="0 0 16 16" aria-hidden="true"><g fill="none" stroke="currentColor" stroke-width="1.3"><circle cx="8" cy="8" r="6.5"/><ellipse cx="8" cy="8" rx="2.8" ry="6.5"/><path d="M1.5 8h13M2.6 4.8h10.8M2.6 11.2h10.8"/></g></svg>
          <span>www.kestreladvisors.example</span>
        </li>
      </ul>
    </div>
  </section>

  <section class="card card--back" aria-label="Back of business card">
    <div class="back-brand">
      <div class="brand-line"><span class="brand-mark"></span>Kestrel Advisors</div>
    </div>
  </section>

</main>
</body>
</html>
```